Cover Art Needed For Digital Single Release

We are looking to have the cover art designed for a new song called "Paper Lanterns". You will find the track attached below in a private TuneVault link so that you can have a listen.
We are thinking of keeping the artwork fairly simple but still want it to catch your eye. Maybe using the song title and artist’s name in a colorful and creative way. (A well-designed font with a bold color scheme, or even something like a mosaic style art piece featuring the title).
We completely welcome any and all creative visions you might have, even if it strays away from the examples given above.
Thank you in advance for your submissions, and we are excited to collaborate with you!
"Paper Lanterns" by Marcus Holloway
https://tunevault.example/marcusxyz/paper-lanterns/s-r7Tq2wLmNcx
Target Market(s)
Teens/Young Adults
Industry/Entity Type
Music
Requirements
Must have
- An eye-catching design
Should not have
- Please do not rely heavily on stock images. We prefer an original design/concept.

```html
<!DOCTYPE html>
<html lang="en">
<head>
<meta charset="UTF-8">
<title>Paper Lanterns — Marcus Holloway</title>
<link href="https://fonts.googleapis.com/css2?family=Archivo+Black&family=EB+Garamond:wght@600&display=swap" rel="stylesheet">
<style>
  :root {
    --amber: #e88a45;
    --peach: #f6c7a0;
    --cream: #fbe6d3;
    --rust: #b8571c;
    --umber: #5a2a0c;
    --cocoa: #3a1a08;
    --glow: #ff8a2a;
  }
  html, body {
    margin: 0;
    width: 1200px;
    height: 1200px;
    overflow: hidden;
    background: var(--cocoa);
  }
  .cover {
    position: relative;
    width: 1200px;
    height: 1200px;
    overflow: hidden;
  }
  .cover-art {
    position: absolute;
    inset: 0;
    display: block;
  }
  .title {
    position: absolute;
    left: 0;
    right: 0;
    top: 330px;
    margin: 0;
    text-align: center;
    font-family: "Archivo Black", sans-serif;
    font-weight: 400;
    text-transform: uppercase;
    color: var(--cocoa);
    line-height: 0.86;
    text-shadow: 0 0 14px var(--glow), 0 0 28px var(--glow), 0 0 4px var(--amber);
  }
  .title-main {
    display: block;
    font-size: 212px;
    letter-spacing: -2px;
  }
  .title-sub {
    display: block;
    font-size: 128px;
    letter-spacing: -1px;
  }
  .artist-tag {
    position: absolute;
    left: 560px;
    top: 1005px;
    padding: 14px 34px 12px;
    background: var(--cream);
    font-family: "EB Garamond", serif;
    font-weight: 600;
    font-size: 52px;
    letter-spacing: 1px;
    color: var(--rust);
    text-transform: uppercase;
    white-space: nowrap;
  }
</style>
</head>
<body>
  <main class="cover">
    <svg class="cover-art" viewBox="0 0 1200 1200" role="img" aria-label="Copper and peach mosaic of irregular hexagonal tiles with light vertical bands">
      <defs>
        <linearGradient id="mosaicTone" x1="0" y1="0" x2="1" y2="1">
          <stop offset="0" stop-color="#f0a878"/>
          <stop offset="0.35" stop-color="#b8602a"/>
          <stop offset="0.6" stop-color="#7a3c14"/>
          <stop offset="0.85" stop-color="#d98a4e"/>
          <stop offset="1" stop-color="#f6c7a0"/>
        </linearGradient>
        <radialGradient id="centreShade" cx="0.5" cy="0.45" r="0.6">
          <stop offset="0" stop-color="#3a1a08" stop-opacity="0.35"/>
          <stop offset="1" stop-color="#3a1a08" stop-opacity="0"/>
        </radialGradient>
      </defs>
      <rect width="1200" height="1200" fill="url(#mosaicTone)"/>
      <rect width="1200" height="1200" fill="url(#centreShade)"/>
    </svg>

    <h1 class="title">
      <span class="title-main">Paper</span>
      <span class="title-sub">Lanterns</span>
    </h1>

    <p class="artist-tag">Marcus Holloway</p>
  </main>
</body>
</html>
```